Business Cards Design for the electrical wholesaler: clean bold dynamic :)

We need a business card design that would follow our latest brand guidelines. As an electrical wholesaler we want to bring a fresh look and feel into the industry. The design should be clean bold and dynamic. It should come alive with the renewed energy of our green colour. Our grey colour should keep things balanced and complement the notion of maturity and responsibility. We employ Lato as a corporate font however are not bound by this font and we’re open to interpretation here.

Target Market(s)

Electrical contractors

Industry/Entity Type

Business

Contact Information for Business Card

Logo
Name & Surname: Olesia Hrybenko
Job Title: Director of Marketing
Email: olesia.hrybenko@mailvex.com
Cell phone: XXX.XXX.XXXX
Address: 20517 - 88 Ave. Edmonton, AB, Canada. T6K 2N8
Business Phone: 780.362.7048
Website: www.kopra.ca

Font styles to use
Other font styles liked:
• Lato

Requirements
Must have
• Logo & website
Nice to have
• Brand elements - some of them you may find in the attached Brand Guidelines (e.g. three lines on the background signifying "W")

```html
<!DOCTYPE html>
<html lang="en">
<head>
<meta charset="utf-8">
<title>Kopra — Business Card</title>
<link rel="stylesheet" href="https://fonts.googleapis.com/css2?family=Lato:ital,wght@0,300;0,400;0,700;1,300&display=swap">
<style>
  :root {
    --backdrop: #d8d0bf;
    --card: #d5dde0;
    --frame-green: #6abf4b;
    --link-green: #4a9a3f;
    --brand-grey: #4d5153;
    --ink: #1f1a14;
    --text-grey: #3a3d3f;
  }
  html, body {
    margin: 0;
    padding: 0;
    width: 1200px;
    height: 1000px;
    overflow: hidden;
    background: var(--backdrop);
    font-family: "Lato", sans-serif;
  }
  .canvas {
    position: relative;
    width: 1200px;
    height: 1000px;
  }
  .card {
    position: absolute;
    left: 352px;
    top: 73px;
    width: 497px;
    height: 853px;
    background: var(--card);
    overflow: hidden;
  }
  .card__brand-block {
    position: absolute;
    left: 0;
    top: 712px;
    width: 232px;
    height: 141px;
    display: block;
    z-index: 1;
  }
  .card__frame {
    position: absolute;
    left: 37px;
    top: 37px;
    width: 422px;
    height: 776px;
    border: 2.5px solid var(--frame-green);
    z-index: 2;
  }
  .logo {
    position: absolute;
    left: 0;
    right: 0;
    top: 170px;
    display: flex;
    justify-content: center;
    align-items: center;
    gap: 16px;
    z-index: 3;
  }
  .logo__dot {
    width: 44px;
    height: 44px;
    border-radius: 50%;
    background: var(--frame-green);
  }
  .logo__name {
    font-weight: 400;
    font-size: 84px;
    line-height: 1;
    color: var(--brand-grey);
    letter-spacing: 1px;
  }
  .person {
    position: absolute;
    left: 0;
    right: 0;
    top: 383px;
    text-align: center;
    margin-left: 6px;
    z-index: 3;
  }
  .person__name {
    margin: 0;
    font-weight: 700;
    font-size: 34px;
    line-height: 40px;
    color: var(--ink);
  }
  .person__title {
    margin: 0;
    font-weight: 300;
    font-style: italic;
    font-size: 29px;
    line-height: 32px;
    color: var(--ink);
  }
  .personal-contact {
    position: absolute;
    left: 0;
    right: 0;
    top: 518px;
    text-align: center;
    font-weight: 300;
    font-size: 22px;
    line-height: 30px;
    color: var(--text-grey);
    margin-left: 6px;
    z-index: 3;
  }
  .company-contact {
    position: absolute;
    right: 44px;
    top: 682px;
    text-align: right;
    color: var(--text-grey);
    z-index: 3;
  }
  .company-contact__address {
    margin: 0;
    font-weight: 400;
    font-size: 21px;
    line-height: 29px;
  }
  .company-contact__phone {
    margin: 8px 0 0;
    font-weight: 400;
    font-size: 22px;
    line-height: 30px;
  }
  .company-contact__web {
    margin: 4px 0 0;
    font-weight: 700;
    font-size: 26px;
    line-height: 32px;
    color: var(--link-green);
  }
</style>
</head>
<body>
<main class="canvas">
  <article class="card">
    <svg class="card__brand-block" viewBox="0 0 232 141" role="img" aria-label="Brand stripe decoration area">
      <rect x="0" y="0" width="232" height="141" fill="var(--brand-grey)"/>
    </svg>

    <div class="card__frame"></div>

    <div class="logo">
      <span class="logo__dot"></span>
      <span class="logo__name">kopra</span>
    </div>

    <header class="person">
      <h1 class="person__name">Olesia Hrybenko</h1>
      <p class="person__title">Director of Marketing</p>
    </header>

    <div class="personal-contact">
      <div class="personal-contact__email">olesia.hrybenko@mailvex.com</div>
      <div class="personal-contact__cell">XXX.XXX.XXXX</div>
    </div>

    <footer class="company-contact">
      <p class="company-contact__address">20517 - 88 Ave. Edmonton,<br>AB, Canada. T6K 2N8</p>
      <p class="company-contact__phone">780.362.7048</p>
      <p class="company-contact__web">www.kopra.ca</p>
    </footer>
  </article>
</main>
</body>
</html>
```